Stationary for Corwin Lattimore | ||
Business card, letterhead, with compliments slip, envelope | ||
Use same font as used in my logo | ||
Corporate Traditional Professional Simple |
[firstname] [surname] | ||
[title] | ||
1 Some Street Sometown Somewhereshire SW23 8SW |
someone@corwinlattimore.example | ||
www.corwinlattimore.example | ||
I am the sole employee at the moment. In the future, I hope to have other employees, so I will add a 'title' section later. Please bear this in mind when positioning the information. I am looking for something that is elegant, professional, minimilistic and tasteful. Please take a look at the website: http://www.corwinlattimore.example using the following credentials to log in: u/n: "pinewhisk" p/w: "pinewhisk847" Please feel free to message me for more information. Most importantly, I want the logo and other key information (like my name?) to be in silver (PMS 877 Metallic). |
I am flexible on this. I want space on my business cards for people to be able to write some information on. | ||

```html
<!DOCTYPE html>
<html lang="en">
<head>
<meta charset="utf-8">
<title>Corwin Lattimore — Business Card</title>
<link rel="stylesheet" href="https://fonts.googleapis.com/css2?family=Cinzel:wght@400;500&display=swap">
<style>
  :root {
    --backdrop: #e8e3da;
    --card-dark: #121212;
    --card-light: #ffffff;
    --silver: #b9bcbf;
    --silver-dark: #8e9194;
    --ink-grey: #6f7275;
    --title-grey: #b5b7b9;
    --edge: #d8d8d8;
  }
  * { margin: 0; padding: 0; box-sizing: border-box; }
  html, body {
    width: 1200px;
    height: 864px;
    overflow: hidden;
    background: var(--backdrop);
    font-family: "Cinzel", "Times New Roman", serif;
  }
  .canvas {
    position: relative;
    width: 1200px;
    height: 864px;
  }
  .card {
    position: absolute;
    top: 282px;
    width: 520px;
    height: 300px;
    border-radius: 6px;
    box-shadow: 0 2px 8px rgba(0, 0, 0, 0.12);
  }

  /* Front */
  .card-front {
    left: 60px;
    background: var(--card-dark);
    border: 4px solid var(--edge);
  }
  .front-logo {
    position: absolute;
    left: 50%;
    top: 50%;
    transform: translate(-50%, -50%);
    display: flex;
    align-items: center;
    gap: 16px;
  }
  .logo-mark {
    width: 14px;
    height: 14px;
    background: var(--silver);
    flex: none;
  }
  .logo-name {
    color: var(--silver);
    font-weight: 400;
    text-transform: uppercase;
    line-height: 1.02;
    letter-spacing: 0.02em;
  }
  .front-logo .logo-name { font-size: 38px; }

  /* Back */
  .card-back {
    left: 620px;
    background: var(--card-light);
    border: 2px solid var(--edge);
  }
  .back-logo {
    position: absolute;
    left: 22px;
    top: 20px;
    display: flex;
    align-items: center;
    gap: 8px;
  }
  .back-logo .logo-mark { width: 7px; height: 7px; background: var(--silver-dark); }
  .back-logo .logo-name { font-size: 15px; color: var(--silver-dark); }

  .holder {
    position: absolute;
    left: 0;
    right: 0;
    top: 120px;
    text-align: center;
  }
  .holder-name {
    font-size: 17px;
    color: var(--silver-dark);
    letter-spacing: 0.04em;
  }
  .holder-title {
    margin-top: 4px;
    font-size: 9px;
    color: var(--title-grey);
    letter-spacing: 0.18em;
  }

  .contact-list {
    position: absolute;
    left: 22px;
    bottom: 30px;
    list-style: none;
    font-size: 7.5px;
    line-height: 1.75;
    color: var(--ink-grey);
    letter-spacing: 0.05em;
  }
  .contact-label {
    display: inline-block;
    width: 46px;
    font-weight: 500;
  }
  .address {
    position: absolute;
    right: 22px;
    bottom: 30px;
    font-style: normal;
    font-size: 7.5px;
    line-height: 1.75;
    color: var(--ink-grey);
    text-align: right;
    letter-spacing: 0.05em;
    text-transform: uppercase;
  }
</style>
</head>
<body>
<main class="canvas">

  <section class="card card-front" aria-label="Business card front">
    <div class="front-logo">
      <span class="logo-mark"></span>
      <div class="logo-name">Corwin<br>Lattimore</div>
    </div>
  </section>

  <section class="card card-back" aria-label="Business card back">
    <div class="back-logo">
      <span class="logo-mark"></span>
      <div class="logo-name">Corwin<br>Lattimore</div>
    </div>

    <div class="holder">
      <div class="holder-name">[FIRSTNAME] [SURNAME]</div>
      <div class="holder-title">TITLE</div>
    </div>

    <ul class="contact-list">
      <li><span class="contact-label">PHONE:</span>44 (0)1234 567890</li>
      <li><span class="contact-label">MOBILE:</span>44 (0)7123 456789</li>
      <li><span class="contact-label">EMAIL:</span>someone@corwinlattimore.example</li>
      <li><span class="contact-label">WEB:</span>www.corwinlattimore.example</li>
    </ul>

    <address class="address">
      1 Some Street<br>
      Sometown<br>
      Somewhereshire<br>
      SW23 8SW
    </address>
  </section>

</main>
</body>
</html>
```